Business Card Design

We need a business card design for a new company based in Melbourne Australia. We are financial broker in finance industry. We provide a wide range of finance solutions to our clients including home loans, commercial loans, business facilities, car loans, equipment loans, invoice finance, etc. The company name is from director's personal name. We would like to have a new company logo that includes TK.

Industry/Entity Type

Business

Contact Information for Business Card

company name: TK & Co Finance Pty Ltd
person's name: Desmond Okafor
role: Managing Director
Mobile: 0417 638 294
fax: 03 9561 4472
Email: desmond.okafor@tkcolending.example
Address: Suite 5/418 Marlow Avenue Elmvale Vic 3174
Credit Licence No.: 718249

```html
<!DOCTYPE html>
<html lang="en">
<head>
<meta charset="utf-8">
<title>TK &amp; Co Finance Pty Ltd — Business Card</title>
<link rel="stylesheet" href="https://fonts.googleapis.com/css2?family=PT+Sans:wght@400;700&display=swap">
<style>
  :root {
    --navy: #1f1a52;
    --green: #7cc242;
    --card: #ffffff;
    --page: #efe9df;
  }
  * { margin: 0; padding: 0; box-sizing: border-box; }
  html, body {
    width: 1189px;
    height: 1200px;
    overflow: hidden;
    background: var(--page);
    font-family: "PT Sans", sans-serif;
    color: var(--navy);
  }
  .canvas { position: relative; width: 1189px; height: 1200px; }
  .card {
    position: absolute;
    left: 171px;
    width: 856px;
    height: 488px;
    background: var(--card);
    border-radius: 21px;
  }
  .card--front { top: 67px; }
  .card--back { top: 627px; }

  .brand { position: absolute; text-align: center; }
  .brand__mark {
    display: block;
    width: 96px;
    height: 96px;
    margin: 0 auto 26px;
    border-radius: 50%;
    background: var(--green);
  }
  .brand__name {
    font-weight: 700;
    font-size: 31px;
    line-height: 1;
    white-space: nowrap;
    color: var(--navy);
  }
  .card--front .brand { left: 0; right: 0; top: 212px; }
  .card--back .brand { left: 0; width: 438px; top: 210px; }

  .divider {
    position: absolute;
    left: 436px;
    top: 106px;
    width: 2px;
    height: 275px;
    background: var(--navy);
  }

  .contact { position: absolute; left: 474px; top: 104px; }
  .contact__name {
    font-weight: 700;
    font-size: 32px;
    line-height: 1;
    letter-spacing: 0.5px;
  }
  .contact__role {
    font-size: 23px;
    line-height: 1;
    color: var(--green);
    margin-top: 4px;
  }
  .contact__address {
    font-size: 22px;
    line-height: 29px;
    margin-top: 30px;
  }
  .contact__list { list-style: none; margin-top: 12px; }
  .contact__item {
    display: flex;
    align-items: center;
    gap: 8px;
    font-size: 22px;
    height: 31px;
  }
  .contact__item--email { font-size: 20.5px; }
  .icon {
    width: 25px;
    height: 25px;
    border-radius: 3px;
    background: var(--green);
    flex: none;
  }
  .contact__licence { font-size: 22px; margin-top: 10px; margin-left: 2px; }
</style>
</head>
<body>
<main class="canvas">

  <section class="card card--front" aria-label="Card front">
    <div class="brand">
      <span class="brand__mark" aria-hidden="true"></span>
      <p class="brand__name">TK &amp; Co Finance Pty Ltd</p>
    </div>
  </section>

  <section class="card card--back" aria-label="Card back">
    <div class="brand">
      <span class="brand__mark" aria-hidden="true"></span>
      <p class="brand__name">TK &amp; Co Finance Pty Ltd</p>
    </div>

    <div class="divider" aria-hidden="true"></div>

    <div class="contact">
      <h1 class="contact__name">DESMOND OKAFOR</h1>
      <p class="contact__role">Managing Director</p>
      <p class="contact__address">Suite 5/418 Marlow Avenue<br>Elmvale Vic 3174</p>
      <ul class="contact__list">
        <li class="contact__item">
          <svg class="icon" viewBox="0 0 25 25" aria-label="Mobile">
            <rect width="25" height="25" rx="3" fill="#7cc242"/>
            <rect x="8" y="4" width="9" height="17" rx="1.5" fill="none" stroke="#fff" stroke-width="1.6"/>
            <rect x="10" y="6.5" width="5" height="4" fill="#fff"/>
            <circle cx="12.5" cy="17.5" r="1.2" fill="#fff"/>
          </svg>
          <span>0417 638 294</span>
        </li>
        <li class="contact__item">
          <svg class="icon" viewBox="0 0 25 25" aria-label="Fax">
            <rect width="25" height="25" rx="3" fill="#7cc242"/>
            <rect x="8" y="4.5" width="9" height="5" fill="#fff"/>
            <rect x="4.5" y="9.5" width="16" height="8" rx="1.5" fill="#fff"/>
            <rect x="8" y="15" width="9" height="5.5" fill="#fff" stroke="#7cc242" stroke-width="1"/>
          </svg>
          <span>03 9561 4472</span>
        </li>
        <li class="contact__item contact__item--email">
          <svg class="icon" viewBox="0 0 25 25" aria-label="Email">
            <rect width="25" height="25" rx="3" fill="#7cc242"/>
            <rect x="4" y="7" width="17" height="11.5" fill="none" stroke="#fff" stroke-width="1.6"/>
            <path d="M4 7 L12.5 13.5 L21 7 M4 18.5 L10 12 M21 18.5 L15 12" fill="none" stroke="#fff" stroke-width="1.4"/>
          </svg>
          <span>desmond.okafor@tkcolending.example</span>
        </li>
      </ul>
      <p class="contact__licence">Licence No.: 718249</p>
    </div>
  </section>

</main>
</body>
</html>
```